Korvel Mining Webpage

Need a website for a copper mining company that is seeking financing and /or partners with small mines. We need a website that will give basic information regarding the property we are seeking financing for, and background information of the owners (about us), current opportunity page that will convey our value added proposition, along with a 'contact us' page.

Please review other mining companies website for ideas
Any clarity needed we will communicate with you, please ask if you are uncertain.

We will likely provide more information as the design develops

Target Market(s)

Investment companies and Mining professionals

Industry/Entity Type

Mining

Number of Pages Required

4 page

Font styles to use
Sans Serif

Colors

Designer to choose colors to be used in the design.

Requirements
Must have
• I am looking to have a template which I can use later as well to add my own content. Please be sure to have each item (designs, links buttons, drop down menus)its own file so I can import into the web formats
• Also please provide primary colors used as RGB values.
• Include a list of fonts used.
• Pages see attached power point slides
• 1) About us - what we do (2 slide of the .ppt attached) need to leave room for a mission and vision statement
• 2) current opportunities (see word document and Slide 5 as results)
• 3) Value Add ideas ( pages 3)
• 4) Management (our photos Slide 4 of the deck) with room to type background information
• 5) Events and current information (this will be a page listing dates of events, and also blog entries.)
• Let us know if you can't open a .ppt file
Nice to have
• Non-cartoonish look, it should be a polished website
• Drop down menu format
• Scrolling format with an image in the background
• Contact information page (see first slide of slide deck)
• Feel free to use the photos as needed through out the site

```html
<!DOCTYPE html>
<html lang="en">
<head>
<meta charset="utf-8">
<title>Korvel Mining</title>
<link rel="stylesheet" href="https://fonts.googleapis.com/css2?family=Cinzel:wght@400;700&family=Lato:wght@400;700;900&display=swap">
<style>
:root{
  --green:#0aa74b;
  --green-dark:#08863c;
  --ink:#222222;
  --text:#444444;
  --muted:#777777;
  --red:#c8202a;
  --orange:#ee7d1c;
  --charcoal:#3a3a3a;
  --footer:#2a2a2a;
  --rock:#3b2c20;
  --light:#eeeeee;
  --white:#ffffff;
}
*{box-sizing:border-box;margin:0;padding:0}
html,body{width:1200px;height:4009px;overflow:hidden;background:var(--white)}
body{font-family:'Lato',sans-serif;color:var(--text)}
.page{position:relative;width:1200px;height:4009px;overflow:hidden}
.abs{position:absolute}
.front{z-index:6}
.shape{position:absolute;left:0;width:1200px}

/* nav */
.main-nav{position:absolute;top:0;left:534px;width:666px;height:48px;background:#1d1d1d;display:flex;align-items:center;padding-left:4px;gap:6px;z-index:7}
.main-nav a{color:var(--white);text-decoration:none;font-size:15px;padding:6px 16px;border-right:1px solid #444;white-space:nowrap}
.main-nav a.active{background:#666}
.main-nav a:last-child{border-right:none}

/* hero */
.hero-photo{position:absolute;left:0;top:0;width:1200px;height:800px;background:linear-gradient(160deg,#b4aba0 0%,#8c8377 35%,#6f675e 60%,#9a9186 100%)}
.brand{position:absolute;left:150px;top:104px;width:260px;z-index:6;display:flex;align-items:center;justify-content:center;gap:10px;white-space:nowrap}
.brand-dot{width:14px;height:14px;border-radius:50%;background:var(--ink);flex:none}
.brand-name{font-family:'Cinzel',serif;font-size:24px;color:var(--ink);letter-spacing:1px;white-space:nowrap}
.hero-title{position:absolute;left:207px;top:388px;width:500px;text-align:center;font-weight:700;font-size:42px;line-height:62px;color:var(--white);z-index:6}
.hero-dots{position:absolute;left:419px;top:584px;display:flex;gap:13px;z-index:6}
.hero-dots span{width:11px;height:11px;border-radius:50%;border:2px solid var(--green);background:transparent}
.hero-dots span.on{background:var(--green)}

/* section titles */
.section-title{font-family:'Cinzel',serif;font-size:32px;letter-spacing:1px;color:var(--ink);white-space:nowrap}
.section-title .accent{color:var(--green)}
.title-rule{width:52px;height:3px;background:var(--green)}

/* about */
.about-title{left:160px;top:690px}
.about-intro{left:160px;top:762px;font-size:14px;font-weight:700;color:var(--ink)}
.about-box{position:absolute;border:2px solid var(--green);background:var(--white);z-index:6}
.about-box h4{color:var(--green);font-size:14px;font-weight:700;margin-bottom:4px}
.about-box ul{list-style:disc;padding-left:18px;font-size:13.5px;color:var(--ink);line-height:20px}
.read-more{position:absolute;left:520px;top:1088px;width:148px;height:42px;background:var(--green);color:var(--white);font-weight:700;font-size:14px;display:flex;align-items:center;justify-content:center;z-index:6}
.read-more-mark{position:absolute;left:484px;top:1096px;width:26px;height:26px;border-radius:50%;background:var(--ink);z-index:6}
.brand-large{position:absolute;left:770px;top:850px;width:340px;text-align:center;z-index:6}
.brand-large .brand-dot{width:240px;height:240px;margin:0 auto 16px;border-radius:50%;background:#5e5e5e}
.brand-large .brand-name{font-size:32px;color:#5e5e5e}

/* solutions */
.solutions-title{left:0;width:1200px;top:1302px;text-align:center}
.solutions-title .section-title{color:var(--white)}
.step{position:absolute;top:1414px;width:180px;text-align:center;z-index:2}
.step-icon{width:108px;height:108px;margin:0 auto;border-radius:50%;background:var(--white);border:6px solid var(--green);display:flex;align-items:center;justify-content:center}
.step-label{margin-top:16px;color:var(--white);font-size:16px;font-weight:700;line-height:21px}
.step-link{position:absolute;top:1468px;width:66px;border-top:3px dotted var(--white);z-index:2}

/* team */
.team-title{left:0;width:1200px;top:1858px;text-align:center}
.member{position:absolute;top:1966px;width:262px;z-index:2}
.member-photo{width:262px;height:163px;background:linear-gradient(180deg,#c9c4bd,#8d8a86)}
.member-name{margin-top:10px;color:var(--red);font-size:21px;font-weight:700}
.member-role{font-size:15px;font-weight:700;color:var(--ink);margin-top:2px}
.member ul{list-style:disc;padding-left:16px;margin-top:14px;font-size:11.5px;line-height:16px;color:var(--text)}
.member li{margin-bottom:10px}

/* banner */
.banner-title{left:0;width:1200px;top:2600px;text-align:center}
.banner-title .section-title{color:var(--white)}
.banner-line{left:0;width:1200px;top:2692px;text-align:center;color:var(--white);font-size:28px;font-weight:700}
.contact-btn{position:absolute;left:560px;top:2760px;width:180px;height:44px;background:var(--green);color:var(--white);font-weight:700;font-size:14px;display:flex;align-items:center;justify-content:center;z-index:2}
.contact-mark{position:absolute;left:522px;top:2768px;width:28px;height:28px;border-radius:50%;background:var(--white);z-index:2}

/* financials */
.fin-title{left:0;width:1200px;top:3000px;text-align:center}
.case{position:absolute;top:3098px;width:272px}
.chart{width:272px;height:186px;border:2px solid #d5d5d5;background:var(--white)}
.case h3{margin-top:18px;color:var(--green);font-size:18px;font-weight:700;line-height:23px}
.case ul{list-style:disc;padding-left:16px;margin-top:14px;font-size:12px;line-height:22px;color:var(--text)}

/* footer */
.footer-head{position:absolute;top:3634px;font-family:'Cinzel',serif;font-size:19px;letter-spacing:1px;color:var(--white);white-space:nowrap}
.footer-head .accent{color:var(--green)}
.footer-rule{position:absolute;top:3666px;width:40px;height:2px;background:var(--green)}
.field{position:absolute;left:160px;width:255px;height:24px;border:1px solid #666;background:#262626;color:#aaa;font-size:11px;padding:5px 8px}
.submit{position:absolute;left:204px;top:3858px;width:96px;height:30px;background:var(--green);color:var(--white);font-weight:700;font-size:13px;display:flex;align-items:center;justify-content:center}
.submit-mark{position:absolute;left:160px;top:3860px;width:26px;height:26px;border-radius:50%;background:var(--white)}
.map{position:absolute;left:468px;top:3700px;width:254px;height:144px;background:linear-gradient(135deg,#e4e4e4,#cfcfcf)}
.contact-line{position:absolute;left:794px;display:flex;gap:12px;color:#dddddd;font-size:13px;line-height:16px}
.contact-line svg{flex:none}
.copyright{position:absolute;left:0;top:3964px;width:1200px;height:45px;background:var(--green);color:var(--white);font-size:12px;padding:14px 160px}
.socials{position:absolute;left:896px;top:3972px;display:flex;gap:10px}
.socials span{width:28px;height:28px;border:1px solid var(--white);border-radius:3px}
</style>
</head>
<body>
<div class="page">

  <!-- hero -->
  <div class="hero-photo" role="img" aria-label="Photo of a yellow mine haul truck and a red pickup on a gravel mine road with safety barriers"></div>
  <svg class="shape" style="top:0;height:800px;z-index:3" viewBox="0 0 1200 800" aria-hidden="true">
    <polygon points="150,0 500,0 325,185" fill="#ffffff" opacity="0.92"/>
    <polygon points="250,330 660,330 455,610" fill="#222" opacity="0.35"/>
    <polygon points="0,510 1200,760 1200,800 0,800" fill="#ffffff"/>
    <polygon points="0,560 0,800 420,800" fill="#f2f2f2"/>
  </svg>
  <nav class="main-nav">
    <a class="active">Home</a><a>About ⌄</a><a>Opportunities</a><a>Our Team</a><a>Events</a><a>Contact Us</a>
  </nav>
  <div class="brand"><span class="brand-dot"></span><span class="brand-name">KORVEL MINING</span></div>
  <h1 class="hero-title">THE GREAT<br>MINING EXPERIENCE<br>COMPANY</h1>
  <div class="hero-dots"><span></span><span class="on"></span><span></span><span></span></div>

  <!-- about -->
  <div class="abs about-title front">
    <div class="section-title"><span class="accent">ABOUT</span> KORVEL MINING</div>
    <div class="title-rule" style="margin-top:6px"></div>
  </div>
  <p class="abs about-intro front">We target neglected assets and turn them into professional operations</p>

  <div class="about-box" style="left:160px;top:820px;width:420px;height:72px;padding:12px 14px">
    <h4>Form a new copper focused Mining Company</h4>
    <ul><li>Acquire majority in small scale producing operations</li></ul>
  </div>
  <svg class="abs front" style="left:548px;top:797px;z-index:7" width="124" height="128" viewBox="0 0 124 128" aria-hidden="true">
    <polygon points="2,2 122,2 62,126" fill="#fff" stroke="#0aa74b" stroke-width="2"/>
    <text x="62" y="22" text-anchor="middle" font-family="Lato,sans-serif" font-weight="700" font-size="12" fill="#0aa74b">Immediate</text>
    <text x="62" y="38" text-anchor="middle" font-family="Lato,sans-serif" font-weight="700" font-size="12" fill="#0aa74b">Operating</text>
    <text x="62" y="54" text-anchor="middle" font-family="Lato,sans-serif" font-weight="700" font-size="12" fill="#0aa74b">Cash</text>
    <text x="62" y="70" text-anchor="middle" font-family="Lato,sans-serif" font-weight="700" font-size="12" fill="#0aa74b">Flow</text>
  </svg>

  <div class="about-box" style="left:300px;top:949px;width:368px;height:108px;padding:10px 14px 10px 20px">
    <h4>Targets are:</h4>
    <ul><li>Under-capitalized</li><li>Hold numerous under-explored concessions</li><li>Located in proven mining districts</li></ul>
  </div>
  <svg class="abs" style="left:160px;top:938px;z-index:7" width="152" height="132" viewBox="0 0 152 132" aria-hidden="true">
    <polygon points="2,2 150,66 2,130" fill="#fff" stroke="#0aa74b" stroke-width="2"/>
    <text x="52" y="48" text-anchor="middle" font-family="Lato,sans-serif" font-weight="700" font-size="11" fill="#0aa74b">High Probability</text>
    <text x="52" y="62" text-anchor="middle" font-family="Lato,sans-serif" font-weight="700" font-size="11" fill="#0aa74b">for added</text>
    <text x="52" y="76" text-anchor="middle" font-family="Lato,sans-serif" font-weight="700" font-size="11" fill="#0aa74b">Value and</text>
    <text x="52" y="90" text-anchor="middle" font-family="Lato,sans-serif" font-weight="700" font-size="11" fill="#0aa74b">Growth</text>
  </svg>

  <div class="read-more-mark"></div>
  <div class="read-more">READ MORE »</div>

  <div class="brand-large"><div class="brand-dot"></div><div class="brand-name">KORVEL MINING</div></div>

  <!-- solutions band -->
  <svg class="shape" style="top:1060px;height:760px;z-index:1" viewBox="0 0 1200 760" aria-hidden="true">
    <defs>
      <linearGradient id="rockTone" x1="0" y1="0" x2="1" y2="1">
        <stop offset="0" stop-color="#4a3828"/><stop offset="0.5" stop-color="#2f2318"/><stop offset="1" stop-color="#3f2f22"/>
      </linearGradient>
    </defs>
    <polygon points="0,23 1200,200 1200,560 0,660" fill="url(#rockTone)" role="img" aria-label="Dark rock face texture background"/>
    <polygon points="600,160 1200,100 1200,290" fill="#0aa74b"/>
    <polygon points="0,620 620,600 0,720" fill="#0aa74b"/>
    <polygon points="1200,560 760,760 1200,760" fill="#f0f0f0"/>
  </svg>
  <div class="abs solutions-title" style="z-index:2">
    <div class="section-title"><span class="accent">OUR</span> SOLUTIONS</div>
    <div class="title-rule" style="margin:8px auto 0"></div>
  </div>

  <div class="step" style="left:122px">
    <div class="step-icon"><svg width="54" height="54" viewBox="0 0 54 54"><ellipse cx="27" cy="20" rx="20" ry="8" fill="none" stroke="#0aa74b" stroke-width="3"/><path d="M7 20 L27 48 L47 20" fill="none" stroke="#0aa74b" stroke-width="3"/></svg></div>
    <div class="step-label">Ownership<br>Consolidation</div>
  </div>
  <div class="step-link" style="left:282px"></div>
  <div class="step" style="left:310px">
    <div class="step-icon"><svg width="54" height="54" viewBox="0 0 54 54"><circle cx="27" cy="22" r="15" fill="none" stroke="#0aa74b" stroke-width="3"/><path d="M19 36 L19 50 M35 36 L35 50" stroke="#0aa74b" stroke-width="3"/></svg></div>
    <div class="step-label">Management With<br>Track Record In District</div>
  </div>
  <div class="step-link" style="left:470px"></div>
  <div class="step" style="left:498px">
    <div class="step-icon"><svg width="54" height="54" viewBox="0 0 54 54"><text x="27" y="42" text-anchor="middle" font-family="Lato,sans-serif" font-weight="900" font-size="40" fill="#0aa74b">$</text></svg></div>
    <div class="step-label">Smart Low<br>Level Capital</div>
  </div>
  <div class="step-link" style="left:658px"></div>
  <div class="step" style="left:686px">
    <div class="step-icon"><svg width="54" height="54" viewBox="0 0 54 54"><path d="M6 44 H48 M14 44 V30 H34 V44 M34 30 L44 10 M44 10 V24" fill="none" stroke="#0aa74b" stroke-width="3"/></svg></div>
    <div class="step-label">Exploration<br>Drilling</div>
  </div>
  <div class="step-link" style="left:846px"></div>
  <div class="step" style="left:874px">
    <div class="step-icon"><svg width="54" height="54" viewBox="0 0 54 54"><rect x="8" y="34" width="7" height="12" fill="#0aa74b"/><rect x="20" y="26" width="7" height="20" fill="#0aa74b"/><rect x="32" y="18" width="7" height="28" fill="#0aa74b"/><path d="M8 24 L40 8" stroke="#0aa74b" stroke-width="3"/></svg></div>
    <div class="step-label">Increased Profits &amp;<br>Company Value</div>
  </div>

  <!-- team -->
  <svg class="shape" style="top:1760px;height:760px;z-index:0" viewBox="0 0 1200 760" aria-hidden="true">
    <polygon points="0,40 420,0 0,320" fill="#f3f3f3"/>
    <polygon points="900,0 1200,0 1200,420" fill="#f3f3f3"/>
    <polygon points="1040,420 1200,260 1200,560" fill="#ebebeb"/>
    <polygon points="0,460 240,560 0,640" fill="#efefef"/>
  </svg>
  <div class="abs team-title" style="z-index:2">
    <div class="section-title"><span class="accent">OUR</span> TEAM</div>
    <div class="title-rule" style="margin:8px auto 0"></div>
  </div>

  <div class="member" style="left:162px">
    <div class="member-photo" role="img" aria-label="Portrait photo of the chief executive officer"></div>
    <div class="member-name">Daniel Harrow</div>
    <div class="member-role">CEO</div>
    <ul>
      <li>13 yr mining experience</li>
      <li>Masters in Mining Engineering from Ridgeline School of Mines.</li>
      <li>Former General Manager Norvale Copper Works</li>
      <li>Proven history of UG mine production growth and reserve increases</li>
      <li>Passed all roles at Open Pit and Underground Operations: Superintendent up to General Manager</li>
    </ul>
  </div>
  <div class="member" style="left:468px">
    <div class="member-photo" role="img" aria-label="Portrait photo of the chief operating officer"></div>
    <div class="member-name">Tomás Velden</div>
    <div class="member-role">COO</div>
    <ul>
      <li>9 yr mining experience</li>
      <li>Current General Manager of Cerro Blanco &amp; Tamsel</li>
      <li>Currently 3% owner of Los Robles</li>
      <li>Born and raised in the district well connected</li>
    </ul>
  </div>
  <div class="member" style="left:774px">
    <div class="member-photo" role="img" aria-label="Portrait photo of the legal counsel"></div>
    <div class="member-name">Clara Ostrand</div>
    <div class="member-role">Legal Consul</div>
    <ul>
      <li>15 yr mining experience</li>
      <li>Local Counsel for Valle Alto Project (Cerro Pardo)</li>
      <li>Local Counsel for Sierra Gris Mine</li>
      <li>Currently 6% owner of Los Robles</li>
    </ul>
  </div>

  <!-- banner -->
  <svg class="shape" style="top:2290px;height:680px;z-index:1" viewBox="0 0 1200 680" aria-hidden="true">
    <polygon points="560,150 1200,10 1200,120" fill="#ee7d1c"/>
    <polygon points="0,196 1200,50 1200,640 0,545" fill="#3a3a3a"/>
    <polygon points="0,196 560,160 0,360" fill="#444444"/>
    <polygon points="0,420 180,545 0,545" fill="#6a2a2a" opacity="0.5"/>
    <polygon points="620,640 1200,640 1200,680" fill="#ececec"/>
  </svg>
  <div class="abs banner-title" style="z-index:2">
    <div class="section-title"><span class="accent">OUR</span> SOLUTIONS</div>
    <div class="title-rule" style="margin:8px auto 0"></div>
  </div>
  <div class="abs banner-line" style="z-index:2">THE SMALL INDEPENDENT MINING COMPANY</div>
  <div class="contact-mark"></div>
  <div class="contact-btn">CONTACT US »</div>

  <!-- financials -->
  <div class="abs fin-title">
    <div class="section-title"><span class="accent">FINANCIALS AND</span> GROWTH CASES</div>
    <div class="title-rule" style="margin:8px auto 0"></div>
  </div>

  <div class="case" style="left:160px">
    <div class="chart">
      <svg width="268" height="182" viewBox="0 0 268 182" aria-label="NPV 8% bar chart" role="img">
        <text x="134" y="18" text-anchor="middle" font-family="Lato,sans-serif" font-weight="700" font-size="11" fill="#222">NPV 8%</text>
        <line x1="30" y1="28" x2="30" y2="150" stroke="#999"/><line x1="30" y1="150" x2="258" y2="150" stroke="#999"/>
        <rect x="60" y="138" width="20" height="12" fill="#f5b43a"/><rect x="82" y="146" width="20" height="4" fill="#e2542a"/>
        <rect x="130" y="126" width="20" height="24" fill="#f5b43a"/><rect x="152" y="140" width="20" height="10" fill="#e2542a"/>
        <rect x="200" y="74" width="20" height="76" fill="#f5b43a"/><rect x="222" y="124" width="20" height="26" fill="#e2542a"/>
        <text x="80" y="164" text-anchor="middle" font-size="9" font-family="Lato,sans-serif" fill="#444">Base Case</text>
        <text x="150" y="164" text-anchor="middle" font-size="9" font-family="Lato,sans-serif" fill="#444">Case 1</text>
        <text x="220" y="164" text-anchor="middle" font-size="9" font-family="Lato,sans-serif" fill="#444">Case 2</text>
        <text x="134" y="177" text-anchor="middle" font-size="8" font-family="Lato,sans-serif" fill="#444">■ 5yr  ■ 8yr</text>
      </svg>
    </div>
    <h3>Base Case Op Improvements</h3>
    <ul>
      <li>Operational Improvements</li>
      <li>Open increase, hire mine and plant managers</li>
      <li>Increase head grade &amp; mill rec.</li>
      <li>Capex = $4M (purchase price)</li>
    </ul>
  </div>
  <div class="case" style="left:465px">
    <div class="chart">
      <svg width="268" height="182" viewBox="0 0 268 182" aria-label="NPV 8% bar chart" role="img">
        <text x="134" y="18" text-anchor="middle" font-family="Lato,sans-serif" font-weight="700" font-size="11" fill="#222">NPV 8%</text>
        <line x1="30" y1="28" x2="30" y2="150" stroke="#999"/><line x1="30" y1="150" x2="258" y2="150" stroke="#999"/>
        <rect x="60" y="138" width="20" height="12" fill="#f5b43a"/><rect x="82" y="146" width="20" height="4" fill="#e2542a"/>
        <rect x="130" y="126" width="20" height="24" fill="#f5b43a"/><rect x="152" y="140" width="20" height="10" fill="#e2542a"/>
        <rect x="200" y="74" width="20" height="76" fill="#f5b43a"/><rect x="222" y="124" width="20" height="26" fill="#e2542a"/>
        <text x="80" y="164" text-anchor="middle" font-size="9" font-family="Lato,sans-serif" fill="#444">Base Case</text>
        <text x="150" y="164" text-anchor="middle" font-size="9" font-family="Lato,sans-serif" fill="#444">Case 1</text>
        <text x="220" y="164" text-anchor="middle" font-size="9" font-family="Lato,sans-serif" fill="#444">Case 2</text>
        <text x="134" y="177" text-anchor="middle" font-size="8" font-family="Lato,sans-serif" fill="#444">■ 5yr  ■ 8yr</text>
      </svg>
    </div>
    <h3>Case 1: Mill + Exploration</h3>
    <ul>
      <li>Base Case operational improvements</li>
      <li>Plant (12.5 kt/month to 17 kt/m)</li>
      <li>Exploration drilling (10,000m)</li>
      <li>Capex = $6.4M (incld. purchase)</li>
    </ul>
  </div>
  <div class="case" style="left:768px">
    <div class="chart">
      <svg width="268" height="182" viewBox="0 0 268 182" aria-label="NPV 8% bar chart" role="img">
        <text x="134" y="18" text-anchor="middle" font-family="Lato,sans-serif" font-weight="700" font-size="11" fill="#222">NPV 8%</text>
        <line x1="30" y1="28" x2="30" y2="150" stroke="#999"/><line x1="30" y1="150" x2="258" y2="150" stroke="#999"/>
        <rect x="60" y="138" width="20" height="12" fill="#f5b43a"/><rect x="82" y="146" width="20" height="4" fill="#e2542a"/>
        <rect x="130" y="126" width="20" height="24" fill="#f5b43a"/><rect x="152" y="140" width="20" height="10" fill="#e2542a"/>
        <rect x="200" y="74" width="20" height="76" fill="#f5b43a"/><rect x="222" y="124" width="20" height="26" fill="#e2542a"/>
        <text x="80" y="164" text-anchor="middle" font-size="9" font-family="Lato,sans-serif" fill="#444">Base Case</text>
        <text x="150" y="164" text-anchor="middle" font-size="9" font-family="Lato,sans-serif" fill="#444">Case 1</text>
        <text x="220" y="164" text-anchor="middle" font-size="9" font-family="Lato,sans-serif" fill="#444">Case 2</text>
        <text x="134" y="177" text-anchor="middle" font-size="8" font-family="Lato,sans-serif" fill="#444">■ 5yr  ■ 8yr</text>
      </svg>
    </div>
    <h3>Mill + Exploration + Mine Development</h3>
    <ul style="margin-top:8px">
      <li>Base Case operational improvements</li>
      <li>Plant (12.5 kt/month to 17 kt/m)</li>
      <li>Exploration drilling (10,000m)</li>
      <li>Capex = $6.4M (incld. purchase)</li>
    </ul>
  </div>

  <!-- footer -->
  <svg class="shape" style="top:3480px;height:529px" viewBox="0 0 1200 529" aria-hidden="true">
    <polygon points="0,20 1200,100 1200,529 0,529" fill="#2a2a2a"/>
    <polygon points="0,20 700,60 0,160" fill="#303030"/>
  </svg>

  <div class="footer-head" style="left:160px"><span class="accent">QUICK</span> INQUIRY</div>
  <div class="footer-rule" style="left:160px"></div>
  <div class="field" style="top:3702px">Name</div>
  <div class="field" style="top:3732px">Phone</div>
  <div class="field" style="top:3762px">Email</div>
  <div class="field" style="top:3792px;height:42px">Message</div>
  <div class="submit-mark"></div>
  <div class="submit">SUBMIT »</div>

  <div class="footer-head" style="left:468px"><span class="accent">LOCATION</span> MAP</div>
  <div class="footer-rule" style="left:468px"></div>
  <div class="map" role="img" aria-label="Street map showing the office location"></div>

  <div class="footer-head" style="left:794px">CONTACT DETAILS</div>
  <div class="footer-rule" style="left:794px"></div>
  <div class="contact-line" style="top:3700px">
    <svg width="14" height="20" viewBox="0 0 14 20"><path d="M7 0 C3 0 0 3 0 7 C0 12 7 20 7 20 C7 20 14 12 14 7 C14 3 11 0 7 0 Z" fill="#0aa74b"/><circle cx="7" cy="7" r="2.5" fill="#2a2a2a"/></svg>
    <div><strong style="color:#fff">Korvel Mining</strong><br>123, Lorem: Adipiscing Elit, Sed Amet<br>Diam Nonummy 012345</div>
  </div>
  <div class="contact-line" style="top:3770px">
    <svg width="18" height="18" viewBox="0 0 18 18"><circle cx="9" cy="9" r="9" fill="#0aa74b"/><path d="M6 5 L8 7 L7 9 C8 10 9 11 10 11 L11 10 L13 12 L12 13 C9 13 5 9 5 6 Z" fill="#2a2a2a"/></svg>
    <div style="font-size:16px;color:#fff">012-345-6789</div>
  </div>
  <div class="contact-line" style="top:3812px">
    <svg width="18" height="18" viewBox="0 0 18 18"><circle cx="9" cy="9" r="9" fill="#0aa74b"/><path d="M6 5 L8 7 L7 9 C8 10 9 11 10 11 L11 10 L13 12 L12 13 C9 13 5 9 5 6 Z" fill="#2a2a2a"/></svg>
    <div style="font-size:16px;color:#fff">012-345-6789</div>
  </div>
  <div class="contact-line" style="top:3858px">
    <svg width="18" height="18" viewBox="0 0 18 18"><circle cx="9" cy="9" r="9" fill="#0aa74b"/><rect x="4" y="6" width="10" height="7" fill="none" stroke="#2a2a2a" stroke-width="1.4"/><path d="M4 6 L9 10 L14 6" fill="none" stroke="#2a2a2a" stroke-width="1.4"/></svg>
    <div>dharrow@korvelmining.net</div>
  </div>

  <div class="copyright">Copyright © 2019 Korvel Mining. All Right Reserved</div>
  <div class="socials"><span></span><span></span><span></span><span></span></div>

</div>
</body>
</html>
```